Taking Steps; Garden Table, Bright Days Rack Card

We want an additional 2 page (front and page) 3.67" x 8.5" rack card. This rack card is now the 2nd of the series . The first one is already completed/finalized and attached (Garden Table Bright Days Rack Card PDF).
Use the text on the word document for the included Taking Steps Rack card. Please use the Garden Table Bright Days Rack card as the template to mimic. We would like all subsequent rack cards to have a similar look and feel.
The document is for older readers. Do not put text over graphics and keep it simple and easy to read with high contrast.
We want some very simple design element(s) incorporated that convey Native American communities or heritage. But NO headdress, teepee graphics, etc. At the top, of the first page we would like a collage of healthy food images. This can include fish, chicken, fresh vegetables, berries, brown rice, etc. Please remember to include the funding statement - it can be in a very small font 6/7 point. For more information about our project, please visit https://plovanta.org/elder-wellness/

```html
<!DOCTYPE html>
<html lang="en">
<head>
<meta charset="utf-8">
<title>Garden Table, Bright Days Rack Card</title>
<link href="https://fonts.googleapis.com/css2?family=Poppins:ital,wght@0,400;0,500;0,600;0,700;0,800;1,600&display=swap" rel="stylesheet">
<style>
:root{
  --maroon:#5b1c16;
  --teal:#25797f;
  --rust:#b84a3f;
  --ink:#2b2b2b;
  --paper:#eef0f0;
  --paper-edge:#e2e5e6;
  --stage:#f4f4f4;
}
*{box-sizing:border-box;margin:0;padding:0}
html,body{width:1200px;height:3230px;overflow:hidden}
body{background:var(--stage);font-family:"Poppins",sans-serif;color:var(--ink);position:relative}
.card{
  position:absolute;top:990px;width:540px;height:1250px;
  background:linear-gradient(90deg,var(--paper) 0%,#f6f7f7 50%,var(--paper-edge) 100%);
  box-shadow:0 6px 22px rgba(0,0,0,.18);
  overflow:hidden;display:flex;flex-direction:column;
}
.card--front{left:40px}
.card--back{left:620px}

/* front */
.food-collage{height:160px;flex:none;background:linear-gradient(100deg,#7a9a4c 0%,#c8802f 35%,#5f8a3a 55%,#e0a07a 75%,#d4b04a 100%)}
.title{font-weight:800;font-size:55px;line-height:1;letter-spacing:.5px;padding:22px 38px 0}
.title .line1{display:block;color:var(--maroon)}
.title .line2{display:block;color:var(--teal);margin-top:2px}
.intro{font-size:15.5px;line-height:1.32;font-weight:500;padding:14px 38px 0}
.subhead{font-size:19px;font-weight:600;color:var(--teal);padding:12px 38px 0}
.subhead b{color:var(--maroon);font-weight:700}
.checklist{list-style:none;padding:8px 38px 0 38px}
.checklist li{display:flex;gap:12px;font-size:15.5px;line-height:1.3;font-weight:500;margin-bottom:10px}
.tick{flex:none;width:18px;height:18px;margin-top:3px}
.doctor-note{color:var(--rust);font-weight:700;font-size:15.5px;line-height:1.3;padding:2px 38px 0}
.band-pattern{height:20px;flex:none;background:linear-gradient(180deg,#eef0f0 0 25%,#9fb5b6 25% 50%,#c3908a 50% 75%,#eef0f0 75%)}
.quote-band{background:var(--maroon);color:#fff;height:150px;flex:none;display:flex;align-items:center;justify-content:space-between;gap:18px;padding:0 26px 0 36px}
.quote{width:300px;min-width:0;font-size:16px;line-height:1.25;font-weight:700;position:relative;padding-top:20px}
.quote .mark{position:absolute;font-size:36px;line-height:1;font-weight:800;top:-10px;left:0}
.quote .mark-end{font-size:30px;line-height:0;vertical-align:-10px;margin-left:8px;font-weight:800}
.quote cite{display:block;font-style:normal;font-weight:500;font-size:14px;margin-top:4px}
.dish-photo{width:128px;height:128px;border-radius:50%;flex:none;background:radial-gradient(circle,#e6c25a 0%,#d88a3a 55%,#f4f0e8 72%);border:4px solid #fff}
.goal-line{color:var(--teal);font-weight:700;font-size:17px;line-height:1.3;padding:20px 38px 0}
.funding{font-size:7.5px;line-height:1.3;padding:8px 38px 0}
.site-footer{margin-top:auto;height:52px;flex:none;background:var(--teal);color:#fff;display:flex;align-items:center;justify-content:center;font-size:17px;letter-spacing:3px;font-weight:500}

/* back */
.back-title{font-weight:800;font-size:42px;line-height:1;padding:54px 0 0 44px}
.back-title .a{color:var(--maroon)}
.back-title .b{color:var(--teal)}
.recipe{display:flex;padding:22px 36px 0 44px;gap:22px}
.recipe-side{width:150px;flex:none}
.recipe-name{color:var(--teal);font-weight:700;font-size:15.5px;line-height:1.15}
.stew-photo{margin-top:14px;width:150px;height:150px;border-radius:50%;background:radial-gradient(circle,#d79a2a 0%,#c27a22 52%,#f5f2ec 66%);box-shadow:0 3px 8px rgba(0,0,0,.2)}
.ingredients h3{font-size:14.5px;font-weight:500;letter-spacing:.3px;margin-bottom:10px}
.ingredients ul{list-style:none}
.ingredients li{display:flex;gap:8px;font-size:15px;line-height:1.28;font-weight:500;margin-bottom:4px}
.method{font-size:15px;line-height:1.32;font-weight:500;padding:30px 44px 0}
.yield{color:var(--maroon);font-weight:700;font-size:15px;padding:14px 44px 0}
.elders-band{margin-top:30px;background:var(--teal);color:#fff;height:132px;flex:none;display:flex;align-items:center;gap:22px;padding:0 36px 0 38px}
.elders-band svg{flex:none}
.elders-band p{font-size:15.5px;line-height:1.3;font-weight:500}
.more-info{text-align:center;padding-top:16px}
.more-info .l1{color:var(--teal);font-weight:500;font-size:15.5px}
.more-info .l2{color:var(--rust);font-weight:500;font-size:15.5px;margin-top:2px}
.source{font-size:15.5px;font-weight:600;margin-top:2px;text-align:center}
.source .hl{color:var(--rust);font-weight:500}
.link-pill{display:block;margin:8px auto 0;width:410px;height:40px;border-radius:20px;background:var(--maroon);color:#fff;font-weight:600;font-size:15.5px;line-height:40px;text-align:center}
.source--second{margin-top:16px}
.org-mark{display:flex;align-items:center;justify-content:center;gap:14px;margin-top:34px}
.org-mark .dot{width:78px;height:78px;border-radius:50%;background:#c8a6a0;flex:none}
.org-mark .name{color:var(--teal);font-weight:600;font-size:19px;line-height:1.15;width:260px}
.back-footer{margin-top:auto;height:120px;flex:none;background:var(--teal);color:#fff;position:relative;padding:14px 200px 0 34px}
.back-footer p{font-size:7.5px;line-height:1.35}
.greens-photo{position:absolute;right:24px;top:-34px;width:150px;height:150px;border-radius:50%;background:radial-gradient(circle,#6f8a3a 0%,#3f6a2a 45%,#7a4a32 62%,#1e1e1e 72%)}
</style>
</head>
<body>

<svg width="0" height="0" style="position:absolute" aria-hidden="true">
  <symbol id="tick-box" viewBox="0 0 18 18">
    <rect x="1" y="3" width="13" height="13" fill="none" stroke="#25797f" stroke-width="1.8"/>
    <path d="M4 9.5l3.5 3.5L17 2" fill="none" stroke="#b84a3f" stroke-width="2.4" stroke-linecap="round" stroke-linejoin="round"/>
  </symbol>
</svg>

<article class="card card--front">
  <div class="food-collage" role="img" aria-label="Collage of healthy foods: salad, vegetables, grilled chicken, salmon, nuts and avocado"></div>
  <h1 class="title"><span class="line1">GARDEN TABLE</span><span class="line2">BRIGHT DAYS</span></h1>
  <p class="intro">Making small changes in what and how you eat can make you feel better and stay healthier longer. Healthy food choices may be good for your brain, energy, mood, and health.</p>
  <h2 class="subhead">Little changes that make <b>a big difference:</b></h2>
  <ul class="checklist">
    <li><svg class="tick"><use href="#tick-box"/></svg>Start today!</li>
    <li><svg class="tick"><use href="#tick-box"/></svg>Write down what, when, and how much you eat for three days</li>
    <li><svg class="tick"><use href="#tick-box"/></svg>Set SMART goals (Specific, Measurable, Attainable, Relevant &amp; Timebound), like: “I will eat one piece of fruit at breakfast three times this week.”</li>
    <li><svg class="tick"><use href="#tick-box"/></svg>Make just 1 or 2 changes at a time until they become a habit</li>
    <li><svg class="tick"><use href="#tick-box"/></svg>Focus more on eating healthy food versus not eating unhealthy food</li>
    <li><svg class="tick"><use href="#tick-box"/></svg>Make a game plan for the times you get tempted to eat unhealthy foods</li>
    <li><svg class="tick"><use href="#tick-box"/></svg>Involve the whole family in setting goals</li>
    <li><svg class="tick"><use href="#tick-box"/></svg>Name your main reason to eat healthier and feel better, like “More energy to go to church and tribal cultural events.”</li>
  </ul>
  <p class="doctor-note">Talk to your doctor about healthier eating to make you feel better and stay healthier longer.</p>
  <div class="band-pattern" style="margin-top:16px" role="img" aria-label="Decorative band in teal and rust tones"></div>
  <div class="quote-band">
    <blockquote class="quote"><span class="mark">“</span>When it comes to traditional foods, for me it’s something more than just food, it’s my heritage.<span class="mark-end">”</span>
      <cite>Lorena Vail (Mesa Ridge Nation)</cite>
    </blockquote>
    <div class="dish-photo" role="img" aria-label="Plate of a traditional dish with vegetables"></div>
  </div>
  <p class="goal-line">Making small, practical changes can help you achieve your health goals.</p>
  <p class="funding">This product is supported by the Regional Community Health Fund (RCHF) as part of a financial assistance award totaling $412,500 with 100 percent funded by RCHF. The contents are those of the author(s) and do not necessarily represent the official views of, nor an endorsement, by RCHF or the U.S. Government.</p>
  <footer class="site-footer">www.plovanta.org</footer>
</article>

<article class="card card--back">
  <h2 class="back-title"><span class="a">MAKE THIS</span> <span class="b">AT HOME</span></h2>
  <div class="recipe">
    <div class="recipe-side">
      <p class="recipe-name">O’odham White Tepary Bean Stew</p>
      <div class="stew-photo" role="img" aria-label="Bowl of white tepary bean stew"></div>
    </div>
    <div class="ingredients">
      <h3>INGREDIENTS:</h3>
      <ul>
        <li><svg class="tick"><use href="#tick-box"/></svg><span>1 cup dried tepary beans, rinsed &amp; picked through (substitute Navy Beans or Great Northern beans)</span></li>
        <li><svg class="tick"><use href="#tick-box"/></svg><span>10 cups of water</span></li>
        <li><svg class="tick"><use href="#tick-box"/></svg><span>1 tsp. salt</span></li>
        <li><svg class="tick"><use href="#tick-box"/></svg><span>1 lb. oxtails, beef short ribs, deer, rabbit, or chicken</span></li>
      </ul>
    </div>
  </div>
  <p class="method">Put beans, water, and salt in a stockpot. Bring to a boil, reduce heat and simmer, covered, for one hour and a half. Add meat to the bean mixture, cover and cook for one more hour, or until beans are tender and meat is falling off the bone. If using a crockpot, place water and all other ingredients in the pot, cover, and set to high. Cook for 8 hours or until the meat is falling off the bone and the beans are tender.</p>
  <p class="yield">Makes 8 – 10 cups</p>
  <div class="elders-band">
    <svg width="56" height="66" viewBox="0 0 56 66" aria-hidden="true">
      <g fill="none" stroke="#fff" stroke-width="2.4" stroke-linecap="round">
        <path d="M28 14c-9 0-15 7-15 15 0 6 3 9 6 12 2 2 3 4 3 7h12c0-3 1-5 3-7 3-3 6-6 6-12 0-8-6-15-15-15z"/>
        <path d="M22 54h12M23 59h10M26 48v-10l2-3 2 3v10"/>
        <path d="M28 2v6M8 10l4 4M48 10l-4 4M2 29h6M48 29h6"/>
      </g>
    </svg>
    <p>Elders are our keepers of traditional knowledge about food and ways of life. You play an important role in sharing this knowledge with younger generations.</p>
  </div>
  <div class="band-pattern" role="img" aria-label="Decorative band in teal and rust tones"></div>
  <div class="more-info">
    <p class="l1">For More Information</p>
    <p class="l2">About Goal Setting</p>
  </div>
  <p class="source"><span class="hl">Harvest Nutrition</span> Council</p>
  <span class="link-pill">https://plovanta.org/goal-video</span>
  <p class="source source--second"><span class="hl">Riverbend Health</span> Institute</p>
  <span class="link-pill">https://plovanta.org/smart-goals</span>
  <div class="org-mark">
    <span class="dot"></span>
    <span class="name">PLOVANTA ELDER WELLNESS CENTER</span>
  </div>
  <footer class="back-footer">
    <p>This product is supported by the Regional Community Health Fund (RCHF) as part of a financial assistance award totaling $412,500 with 100 percent funded by RCHF. The contents are those of the author(s) and do not necessarily represent the official views of, nor an endorsement, by RCHF or the U.S. Government.</p>
    <div class="greens-photo" role="img" aria-label="Bowl of broccoli and roasted vegetables"></div>
  </footer>
</article>

</body>
</html>
```